Zolna Radio Web

Radio Station web site to include but not limited:

- About US (company profile)
- Now playing (from our streaming server link)
- Upcoming events with a possibility to have photos for advertisement purpose, etc...
- Language switch from Russian to English

- Member section:
Login module (with new user name and password, forgot password, etc...)
Login module with Chatterloop details
Request a song
LIKE feature with Chatterloop...

- Social links: (along with Chatterloop LIKE)
Send page to a friend
share / chatterloop share
Chat section where all logged users can chat in the same room.

- Contact us (Radio email ID )
- TabQuill - TuneBrick compatible

2 Websites were found to match the design that we re looking for:
http://www.vetrika.com and
http://marcotelvin.com

The site colors shall be matching and ongoing with our logo colors and designs as well.

Thanks,
Zolna Radio Team
Updates

Extended dead line and project is guaranteed.

Project Deadline Extended
Reason: Need more designs for review...

Industry/Entity Type

Radio

Requirements
Must have
• Chatterloop Login
Chatterloop LIKE
Users Chat Section
Language Switch
TabQuill - TuneBrick compatible
Nice to have
• Less pages switch. Initial shall be to switch from russian to english (or EN to RU) but the less pages we flip, the better. (except pop ups for log in, request a song, etc...)

```html
<!DOCTYPE html>
<html lang="en">
<head>
<meta charset="utf-8">
<title>Zolna Radio</title>
<link href="https://fonts.googleapis.com/css2?family=PT+Sans:wght@400;700&family=Arimo:wght@400;700&display=swap" rel="stylesheet">
<style>
:root{
  --page-dark:#151719;
  --nav-top:#27a6e8;
  --nav-bottom:#0a82cf;
  --white:#ffffff;
  --paper:#faf8f2;
  --gutter:#dfe6e6;
  --text:#333333;
  --muted:#666666;
  --red:#d52b1e;
  --link:#0a6fb0;
  --star:#1a8ed6;
  --row-blue:#d4ebf7;
  --row-beige:#f2ecdd;
  --tab-off:#efe9d6;
  --line:#c9c9c9;
  --btn-top:#2b8ccc;
  --btn-bottom:#0c5f99;
  --newsletter:#3d3d3d;
  --footer-top:#0f92d8;
  --footer-bottom:#063e63;
}
*{box-sizing:border-box;margin:0;padding:0}
html,body{width:1200px;height:1085px;overflow:hidden}
body{position:relative;background:repeating-linear-gradient(135deg,#1b1d20 0 3px,#131416 3px 6px);font-family:"Arimo",Arial,sans-serif;color:var(--text)}
.abs{position:absolute}
.header-photo{left:470px;top:0;width:618px;height:110px;background:linear-gradient(90deg,rgba(20,22,26,0) 0%,#3a2a4a 35%,#6a3e63 60%,#c99a8f 90%,#e0b7a5 100%)}
.logo{left:130px;top:4px;display:flex;align-items:center;gap:10px}
.logo-mark{width:104px;height:104px;border-radius:50%;background:#0f3f86;border:4px solid #bfc6cc}
.logo-name{font-family:"PT Sans",sans-serif;font-size:20px;color:#fff;font-weight:700}
.nav{left:110px;top:110px;width:996px;height:38px;background:linear-gradient(var(--nav-top),var(--nav-bottom));display:flex}
.nav a{color:#fff;text-decoration:none;font-family:"PT Sans",sans-serif;font-size:16px;display:flex;align-items:center;justify-content:center;border-right:1px solid #0b6fb0;box-shadow:1px 0 0 #4ab9ef}
.nav a:last-child{border:none;box-shadow:none}
.fold{top:148px;width:0;height:0;border-top:18px solid #0a6aa8}
.fold.l{left:110px;border-left:18px solid transparent}
.fold.r{left:1088px;border-right:18px solid transparent}
.content{left:128px;top:148px;width:960px;height:774px;background:var(--gutter)}
.topbar{left:128px;top:148px;width:960px;height:56px;background:var(--paper);border-bottom:1px dashed #cfcfcf}
.now-tag{left:143px;top:167px;width:130px;height:22px;background:var(--red);clip-path:polygon(0 0,92% 0,100% 50%,92% 100%,0 100%);color:#fff;font-size:11px;padding:4px 0 0 33px;border-radius:4px 0 0 4px}
.now-time{left:283px;top:173px;font-size:11px;font-weight:700;color:#333}
.now-title{left:337px;top:172px;font-size:12px;font-weight:700;color:var(--red)}
.play{width:16px;height:16px;border-radius:50%;border:1px solid #9bbad0;background:#f2f7fb}
.search{left:774px;top:167px;width:235px;height:21px;border:1px solid #a9a9a9;background:#fff;font-size:11px;color:#666;padding:4px 0 0 28px}
.btn-blue{background:linear-gradient(var(--btn-top),var(--btn-bottom));color:#fff;border-radius:3px;font-size:12px;display:flex;align-items:center;justify-content:center}
.main{left:128px;top:204px;width:960px;height:313px;background:#fff}
.hero{left:140px;top:224px;width:627px;height:293px;background:linear-gradient(110deg,#e98061,#d9664a 45%,#b7543a 75%,#8c3a24)}
.panel{background:#fff;border:1px solid #d6d6d6}
.tab{position:absolute;font-family:"PT Sans",sans-serif;font-size:15px;display:flex;align-items:center;justify-content:center;color:#222}
.tab.off{background:linear-gradient(#f6f2e6,#e8e1c9);border-left:1px solid #d6d0bd;border-bottom:1px solid #d6d0bd}
.thumb{border:1px solid #cfcfcf;border-radius:4px;background:linear-gradient(#9a9089,#5a524f)}
.ev-time{font-size:10px;font-weight:700;color:#222}
.stars{color:var(--star);font-size:10px;letter-spacing:-1px}
.stars i{color:#c8c8c8;font-style:normal}
.ev-text{font-size:10.5px;line-height:14px;color:#222;width:182px}
.more{left:990px;top:484px;font-size:12px;color:var(--link);text-decoration:underline}
.col{top:545px;height:377px;background:#fff}
.heading{font-family:"PT Sans",sans-serif;font-size:15px;color:#222}
.song{left:142px;width:285px;height:30px;border-radius:0 15px 15px 0}
.song.b{background:linear-gradient(90deg,#fff,var(--row-blue))}
.song.e{background:linear-gradient(90deg,#fff,var(--row-beige))}
.song .art{position:absolute;left:0;top:0;width:31px;height:30px;border-radius:4px;background:linear-gradient(#777,#333)}
.song .artist{position:absolute;left:40px;top:1px;font-size:11px;font-weight:700;color:#333}
.song .title{position:absolute;left:40px;top:16px;font-size:10.5px;color:#333}
.song .title span{color:#888}
.song .play{position:absolute;left:201px;top:6px}
.song .stars{position:absolute;left:226px;top:8px}
.label{font-size:12px;color:#555}
.field{background:#fff;border:1px solid #b9b9b9;height:22px}
.newsletter{left:451px;top:755px;width:314px;height:167px;background:var(--newsletter)}
.btn-grey{background:linear-gradient(#fafafa,#d4d4d4);border:1px solid #9a9a9a;border-radius:3px;font-size:12px;color:#222;display:flex;align-items:center;justify-content:center}
.rule{height:1px;background:#d6d6d6}
.social{left:797px;top:879px;display:flex;gap:8px}
.social span{width:22px;height:22px;border-radius:4px;background:linear-gradient(#e6eef4,#a9c3d6);border:1px solid #8aa9bf}
.footer{left:0;top:922px;width:1200px;height:163px;background:linear-gradient(var(--footer-top),var(--footer-bottom))}
.footer h2{font-family:"PT Sans",sans-serif;font-weight:400;font-size:19px;color:#fff}
.footer p{font-size:12px;line-height:14px;color:#fff}
</style>
</head>
<body>
<div class="abs header-photo" role="img" aria-label="Glowing studio lights and a listener wearing headphones"></div>
<div class="abs logo"><span class="logo-mark"></span><span class="logo-name">Zolna Radio</span></div>

<nav class="abs nav">
  <a style="width:131px">Home</a><a style="width:144px">About Us</a><a style="width:133px">Services</a><a style="width:126px">Photos</a><a style="width:121px">Downloads</a><a style="width:100px">Links</a><a style="width:103px">Login</a><a style="width:138px">Contact Us</a>
</nav>
<div class="abs fold l"></div><div class="abs fold r"></div>

<div class="abs content"></div>
<div class="abs topbar"></div>
<div class="abs now-tag">Now Playing</div>
<div class="abs now-time">7:00–9:20</div>
<div class="abs now-title">Lorem ipsum dolor consec &gt;&gt;</div>
<div class="abs play" style="left:507px;top:171px"></div>
<div class="abs search">Search songs</div>
<svg class="abs" style="left:781px;top:171px" width="12" height="12" viewBox="0 0 12 12"><circle cx="5" cy="5" r="3.5" fill="none" stroke="#555" stroke-width="1.5"/><line x1="7.5" y1="7.5" x2="11" y2="11" stroke="#555" stroke-width="1.5"/></svg>
<div class="abs btn-blue" style="left:1016px;top:166px;width:52px;height:22px;border-radius:1px;font-size:11px">Search</div>

<div class="abs main"></div>
<div class="abs hero" role="img" aria-label="Smiling listener wearing headphones against a warm orange backdrop"></div>

<section class="abs panel" style="left:774px;top:224px;width:299px;height:291px">
  <div class="tab" style="left:0;top:0;width:150px;height:33px">Upcoming Events</div>
  <div class="tab off" style="left:150px;top:0;width:148px;height:33px">Chat Room</div>
</section>
<div class="abs thumb" style="left:789px;top:277px;width:77px;height:76px" role="img" aria-label="Host portrait"></div>
<div class="abs ev-time" style="left:879px;top:276px">12:40–13:40</div>
<div class="abs stars" style="left:1008px;top:275px">★★★★<i>★</i></div>
<p class="abs ev-text" style="left:879px;top:295px">Lorem ipsum dolor sit amet, consectetur adipisicing elit, sed do eiusmod tempor incididunt ut labore et dolore magna aliqua.</p>
<div class="abs thumb" style="left:789px;top:387px;width:77px;height:76px;background:linear-gradient(#b58aa0,#5b3650)" role="img" aria-label="Singer portrait"></div>
<div class="abs ev-time" style="left:879px;top:386px">15:00–16:00</div>
<div class="abs stars" style="left:1008px;top:385px">★★★★★</div>
<p class="abs ev-text" style="left:879px;top:407px">Lorem ipsum dolor sit amet, consectetur adipisicing elit, sed do eiusmod tempor incididunt ut labore et dolore magna aliqua.</p>
<a class="abs more">Read More..</a>

<!-- Top songs -->
<section class="abs col" style="left:128px;width:314px">
  <div class="tab" style="left:0;top:0;width:157px;height:32px">Top 10 Songs</div>
  <div class="tab off" style="left:157px;top:0;width:157px;height:32px">View Playlist</div>
</section>
<div class="abs song b" style="top:592px"><span class="art"></span><span class="artist">Velmora</span><span class="title">Holdover <span>4:18</span></span><span class="play"></span><span class="stars">★★★★★</span></div>
<div class="abs song e" style="top:632px"><span class="art"></span><span class="artist">Quietwire</span><span class="title">Low and Wet <span>5:27</span></span><span class="play"></span><span class="stars">★★★★★</span></div>
<div class="abs song b" style="top:672px"><span class="art"></span><span class="artist">Ладья</span><span class="title">Вдаль <span>3:45</span></span><span class="play"></span><span class="stars">★★★★<i>★</i></span></div>
<div class="abs song e" style="top:712px"><span class="art"></span><span class="artist">Стриж и Ко</span><span class="title">О ветре <span>5:09</span></span><span class="play"></span><span class="stars">★★★★<i>★</i></span></div>
<div class="abs song b" style="top:752px"><span class="art"></span><span class="artist">The Gates</span><span class="title">The edge <span>6:23</span></span><span class="play"></span><span class="stars">★★★★<i>★</i></span></div>
<div class="abs song e" style="top:792px"><span class="art"></span><span class="artist">Brann</span><span class="title">Stranger in Old Harbor <span>7:12</span></span><span class="play"></span><span class="stars">★★★<i>★★</i></span></div>
<div class="abs song b" style="top:832px"><span class="art"></span><span class="artist">Heavy Signal</span><span class="title">Slow Currents <span>5:48</span></span><span class="play"></span><span class="stars">★★★<i>★★</i></span></div>
<div class="abs song e" style="top:872px"><span class="art"></span><span class="artist">O-ho</span><span class="title">Longwaves <span>3:40</span></span><span class="play"></span><span class="stars">★★★<i>★★</i></span></div>

<!-- Request a song -->
<section class="abs col" style="left:451px;width:314px"></section>
<div class="abs heading" style="left:464px;top:554px">Request a Song</div>
<div class="abs rule" style="left:451px;top:579px;width:314px"></div>
<div class="abs label" style="left:472px;top:608px">Film Name</div>
<div class="abs field" style="left:552px;top:604px;width:190px"></div>
<div class="abs label" style="left:472px;top:640px">Artist</div>
<div class="abs field" style="left:552px;top:635px;width:190px"></div>
<div class="abs label" style="left:472px;top:671px">Your Name</div>
<div class="abs field" style="left:552px;top:666px;width:190px"></div>
<div class="abs btn-blue" style="left:551px;top:703px;width:95px;height:27px">Send Request</div>

<div class="abs newsletter"></div>
<div class="abs heading" style="left:464px;top:766px;color:#fff">Newsletter</div>
<div class="abs rule" style="left:451px;top:790px;width:314px;background:#555"></div>
<div class="abs field" style="left:467px;top:810px;width:272px;height:25px;font-size:12px;color:#333;padding:5px 8px">Enter your mail ID</div>
<div class="abs btn-grey" style="left:570px;top:857px;width:74px;height:25px">Subscribe</div>

<!-- Login -->
<section class="abs col" style="left:774px;width:314px">
  <div class="tab" style="left:0;top:0;width:157px;height:32px">Login Form</div>
  <div class="tab off" style="left:157px;top:0;width:157px;height:32px">Chatterloop Login</div>
</section>
<div class="abs label" style="left:796px;top:608px">User Name</div>
<div class="abs field" style="left:876px;top:604px;width:190px"></div>
<div class="abs label" style="left:796px;top:640px">Password</div>
<div class="abs field" style="left:876px;top:635px;width:190px"></div>
<div class="abs btn-blue" style="left:876px;top:673px;width:65px;height:27px">Login</div>
<a class="abs" style="left:958px;top:679px;font-size:12px;color:var(--link);text-decoration:underline">Forget Password?</a>

<div class="abs heading" style="left:786px;top:739px">Send Page to Friend</div>
<div class="abs rule" style="left:774px;top:762px;width:314px"></div>
<div class="abs field" style="left:795px;top:781px;width:215px;height:26px;font-size:12px;color:#333;padding:6px 8px">Enter your mail ID</div>
<div class="abs btn-blue" style="left:1009px;top:780px;width:55px;height:27px">Send</div>

<div class="abs heading" style="left:786px;top:834px">Connect with us</div>
<div class="abs rule" style="left:774px;top:857px;width:314px"></div>
<div class="abs social" aria-label="Social sharing links"><span></span><span></span><span></span><span></span><span></span><span></span><span></span><span></span><span></span></div>

<footer class="abs footer">
  <h2 class="abs" style="left:130px;top:20px">Contact Us</h2>
  <p class="abs" style="left:131px;top:59px;width:245px">Lorem ipsum dolor sit amet, consectetur adipisicing elit, sed do eiusmod tempor incididunt ut labore et dolore magna aliqua.</p>
  <p class="abs" style="left:131px;top:115px;width:230px">eiusmod tempor incididunt ut labore et dolore magna aliqua.</p>
  <p class="abs" style="left:772px;top:57px">Copyright @ 2011. Zolna Radio.com All Rights Reserved.</p>
  <p class="abs" style="left:775px;top:90px">terms and Conditions | Privacy Policy</p>
</footer>
</body>
</html>
```